Making Maui's Gentle Tides of Welcome Open to Everyone and then add the logo Camp Bright Reach Maui

We need a design to a brochure to promote building and seek donors of the first fully wheelchair accessible camp which would be located on Maui, HI and with a FOCUS on why it needs to be built.
We have a fundraiser on https://www.kindpledgehub.example/education-fundraising/a-haven-for-young-explorers-to-flourish--3/x/58203917 PLEASE SEE THE BRIEF FOR INFO
Updates

Target Market(s)

those with disabilities and their families, or anyone interested in fully accessible facility, rehabilitation after accident

Industry/Entity Type

Education

Requirements
Must have
• Please put in order in tri fold brochure
• Who we Are:
• The Board Members of Keep Rising Onward are dedicated to the need of accessibility for outdoor activities within an educational camp facility. Our Board Members represent a variety of backgrounds, and disabilities.
• Our Mission:
• Keep Rising Onward, Inc is a 501c(3) nonprofit founded in 2004 in Hawaii that is dedicated to helping children, young people and particularly those with mobility impairments reach their own potential, empower dignity, and motivate purposeful living. Our passion is to inspire, educate, and create accessible outdoor facilities.
• We have 5 beautiful acres of leased land located on the West sunny side of the Maui Island. This property is near an accessible part of the ocean
• The Need:
• 53 million individuals with disabilities live in the United States and one billion people with disabilities live around the world. Everyone in their life time is at risk of mobility impairment. This could happen any day, at anytime to anyone. Families that experience catastrophic events or individuals are born with developmental disabilities face enormous challenges. Many families that experience this are financially destroyed and spiritually as well as emotionally exhausted. One of the biggest struggles those with disabilities face is getting enough education. Most individuals with disabilities often are left to feel isolated and alone. The American Disabilities Act was implemented in 1990, but most therapeutic outdoor activities are not accessible to those with disabilities especially on the Hawaiian Islands.
• Building the dream:
• Camp Bright Reach Maui will be a 100% wheelchair accessible and barrier free camp facility that will be built on 5 acres of land in Olowalu, Maui Hawaii. This future farm facility would be used to educate, and enrich the lives of those with disabilities as well as their families and help them heal their emotional, spiritual, and psychological hurt. In an ranch like setting, educational and nurturing programs will be centered around old Hawaiian culture, agricultural history, production, animal care, and teamwork. With a host of innovations for enhanced accessibility such as raised garden beds, and wider pathways those attending the facility would be empowered with more independence. Therapeutic adaptive sporting activities designed for those with physical mobility impairments will be available, like kayaking, paddle boarding, and zip lining.
• Life Time Value:
• This future facility would promote awareness to the community around it about the importance of humanity and education as well as providing inclusion and equality for those with disabilities. Therapeutic outdoor activities will allow those to heal and gain invaluable tools. Participants of the camp would leave with a Keep Rising Onward Attitude, integrating into their communities with positive potential and purposeful living. Together we can walk and roll!
• Where your money will go:
• Phase 1 to pursue a State Special Land Use permit.
• To get the special land use permit together for the Planning Department of Maui, it will cost $20,000.
• Below is a breakdown of the first phase of the permit:
• -Archaeological summary
• -Site survey
• -fulfill legal notification requirements to existing neighbors
• -Traffic Impact analysis
• -Drainage and Erosion Control analysis
• -Waste Water System Design
• -Topographical Design Survey
• -Construction Permitting Phase
• We Need Your Help:
• Join us in this amazing mission by becoming a member of our Keep Rising Onward team. You will leave a legacy of Maui’s first 100% accessible camp.
• A) Ambassador- help spread the word
• B) Build the camp- grab a shovel swing a hammer
• C) Contribute financially
• D) Donate materials and services
• Help support the dream by buying a camp logo t-shirt on CampBrightreachmaui.example
• Keep Rising Onward
• PO BOX 418
• Albany, OR 97358
• 541-555-0147
• CampBrightReachMaui@mailbox.example
• Please include this in someway, like an QR scan or something https://www.kindpledgehub.example/education-fundraising/a-haven-for-young-explorers-to-flourish--3
Nice to have
• Things we would like- kids at a campfire someone in a wheelchair there laughing
Should not have
• NO photos of Dale Morrow unless its the one of him and the waterfall phone number 541-555-0182 or pinecresthollow@mailbox.example these are both wrong contact info

```html
<!DOCTYPE html>
<html lang="en">
<head>
<meta charset="utf-8">
<title>Camp Bright Reach Maui – Trifold Brochure</title>
<link rel="stylesheet" href="https://fonts.googleapis.com/css2?family=Open+Sans:ital,wght@0,400;0,600;0,700;1,400;1,600&family=Roboto+Condensed:wght@300;700&display=swap">
<style>
  :root{
    --bg:#d9d9db;
    --paper:#ffffff;
    --cream:#fbf0c2;
    --cream-light:#fdf7de;
    --blue:#1d64ad;
    --blue-dark:#174f8a;
    --green:#7db63c;
    --green-dark:#5f9a2a;
    --ink:#2d3340;
    --muted:#5b6170;
  }
  *{box-sizing:border-box;margin:0;padding:0}
  html,body{width:1200px;height:1200px;overflow:hidden}
  body{background:var(--bg);font-family:"Open Sans",sans-serif;color:var(--ink);
       display:flex;flex-direction:column;align-items:center;justify-content:center;gap:34px}
  .spread{position:relative;width:760px;height:560px;display:grid;grid-template-columns:repeat(3,1fr);
          background:var(--paper);box-shadow:0 10px 30px rgba(0,0,0,.18);overflow:hidden}
  .panel{position:relative;padding:22px 18px;font-size:7.4px;line-height:1.45;border-right:1px solid rgba(0,0,0,.06);overflow:hidden}
  .panel:last-child{border-right:0}
  .panel--cream{background:linear-gradient(180deg,var(--cream-light),var(--cream))}
  h2{font-size:11px;font-weight:700;color:var(--blue);margin-bottom:6px}
  p{margin-bottom:7px;text-align:justify}
  .photo{border-radius:10px;box-shadow:0 2px 6px rgba(0,0,0,.25)}
  .logo{display:flex;align-items:center;justify-content:center;gap:6px;font-weight:700;color:var(--blue);font-size:12px;letter-spacing:.3px}
  .logo-dot{width:12px;height:12px;border-radius:50%;background:var(--green)}

  /* outside, panel 1 */
  .mission-band{margin:10px -18px;background:var(--blue);color:#fff;font-style:italic;font-size:8.5px;padding:8px 18px;line-height:1.35}
  .lead{font-style:italic;font-size:8.2px;margin-bottom:8px}
  .lead--blue{color:var(--blue);font-size:9.4px;line-height:1.35}
  .boy-photo{position:absolute;left:0;right:0;bottom:0;height:175px;
             background:linear-gradient(160deg,#f3e1a0 0%,#c9b89a 45%,#3d4a72 75%,#2a2f48 100%)}

  /* outside, panel 2 */
  .panel--plans{padding:14px 12px 0}
  .floor-plan{height:170px;border:1px solid #c9ccd2;background:repeating-linear-gradient(0deg,#fff 0 14px,#eef0f3 14px 15px);border-radius:4px}
  .site-plan{margin-top:10px;height:300px;border:1px solid #c9ccd2;border-radius:4px;
             background:radial-gradient(ellipse 38% 42% at 45% 45%,#9ccc5a 0%,#c3e08d 55%,#fafaf7 80%)}
  .contact-band{position:absolute;left:0;right:0;bottom:0;height:46px;background:var(--blue-dark);color:#fff;
                display:flex;align-items:center;justify-content:center;gap:6px;font-size:8px;font-style:italic}

  /* outside, panel 3 (cover) */
  .panel--cover{padding:0;display:flex;flex-direction:column}
  .cover-top{height:90px;display:flex;align-items:center;justify-content:center;position:relative}
  .cover-top svg{position:absolute;left:0;bottom:0}
  .cover-photo{height:205px;background:linear-gradient(170deg,#fbf3dd 0%,#eedfbd 35%,#c7b08a 65%,#8b7f62 100%)}
  .cover-headline{background:var(--green);color:#fff;padding:22px 20px;height:185px;font-family:"Roboto Condensed",sans-serif}
  .cover-headline .l1{font-size:22px;font-weight:700;color:var(--blue-dark)}
  .cover-headline .l2{font-size:33px;font-weight:700;line-height:1}
  .cover-headline .l3{font-size:22px;font-weight:700;color:var(--blue-dark)}
  .cover-headline .l4{font-size:33px;font-weight:300;line-height:1}
  .cover-url{flex:1;display:flex;align-items:center;justify-content:center;color:var(--blue);font-weight:700;font-size:8.5px;letter-spacing:.5px}

  /* inside */
  .waves{position:absolute;left:0;bottom:0;width:760px;height:90px;pointer-events:none}
  .thanks{color:var(--blue);font-weight:700;font-size:9px;line-height:1.35;margin:6px 0 8px}
  .waterfall{height:118px;background:linear-gradient(150deg,#3f6b3a 0%,#6f9b52 40%,#a6c6d6 60%,#5a7a45 100%)}
  .steps{list-style:none;font-size:8px;margin-bottom:12px}
  .steps li{padding-left:9px;position:relative;margin-bottom:2px}
  .steps li::before{content:"";position:absolute;left:0;top:4px;width:4px;height:4px;border-radius:50%;background:var(--blue)}
  .stage-photo-a{height:88px;background:linear-gradient(120deg,#dfe4ea 0%,#9aa6b4 45%,#5b4a3f 100%);margin-bottom:10px}
  .stage-photo-b{height:88px;background:linear-gradient(120deg,#1d1a22 0%,#8a3b26 50%,#e2a24e 100%);margin-left:14px}
  .duo{display:flex;gap:8px;margin:4px 0 10px}
  .duo .photo{flex:1;height:58px}
  .portrait-a{background:linear-gradient(135deg,#e5e5e5,#6d6d6d)}
  .portrait-b{background:linear-gradient(135deg,#f1c9a2,#8a4a2e)}
  .inside-logo{margin-top:12px}
</style>
</head>
<body>

<section class="spread spread--outside">
  <div class="panel panel--cream">
    <h2>Our Mission</h2>
    <p>Keep Rising Onward, Inc is a 501c(3) nonprofit founded in 2004 in Hawaii that is dedicated to helping children, young people and particularly those with mobility impairments reach their own potential, empower dignity, and motivate purposeful living. Our passion is to inspire, educate, and create accessible outdoor facilities where families can grow together and learn how to thrive.</p>
    <div class="mission-band">Camp Bright Reach Maui A place for children with disabilities &amp; their families to THRIVE</div>
    <p class="lead">Providing the tools of success for individuals with disabilities in an educational outdoor setting.</p>
    <p class="lead lead--blue">We have 5 acres of land now we are waiting to have funds to create an environment where those with disabilities are encouraged to expand and explore new possibilities</p>
    <div class="boy-photo" role="img" aria-label="Photo of a smiling boy in a wheelchair holding notebooks"></div>
  </div>

  <div class="panel panel--plans">
    <div class="floor-plan" role="img" aria-label="Architectural floor plan of the camp lodge"></div>
    <div class="site-plan" role="img" aria-label="Site plan of the five acre camp with landscaped paths and trees"></div>
    <div class="contact-band">
      <svg width="13" height="9" viewBox="0 0 13 9" aria-hidden="true"><rect x=".5" y=".5" width="12" height="8" fill="none" stroke="#fff"/><path d="M.5 .5 6.5 5 12.5 .5" fill="none" stroke="#fff"/></svg>
      support@campbrightreachmaui.example
    </div>
  </div>

  <div class="panel panel--cover">
    <div class="cover-top">
      <div class="logo"><span class="logo-dot"></span>Camp Bright Reach Maui</div>
      <svg width="254" height="24" viewBox="0 0 254 24" aria-hidden="true"><path d="M0 8 Q120 30 254 4" fill="none" stroke="var(--blue)" stroke-width="2"/></svg>
    </div>
    <div class="cover-photo" role="img" aria-label="Photo of smiling seniors outdoors, one in a wheelchair"></div>
    <div class="cover-headline">
      <div class="l1">A place</div>
      <div class="l2">FOR CHILDREN</div>
      <div class="l3">with disabilities</div>
      <div class="l4">TO THRIVE</div>
    </div>
    <div class="cover-url">www.campbrightreachmaui.example</div>
  </div>
</section>

<section class="spread spread--inside">
  <div class="panel">
    <h2>Where will your donations go?</h2>
    <p>To get the special land use permit together for the Planning Department of Maui, it will cost $20,000. We estimate the need for 3 septic systems and tanks at the individual price of $19,000 for a total of $58,000. Excavating, leveling, and basic infrastructure will cost another $22,000. Any extra money left over will be applied to additional impact studies if required by the county. If they are not needed we will work with local schools planting and growing trees, fruits, and "Canoe" plants (Polynesian-introduced Hawaiian plants) as well as indigenous plants to Hawaii.</p>
    <h2>Life Time Value</h2>
    <p>To instill a Keep Rising Onward Attitude among the Youth and those with disabilities to not only just survive, but THRIVE in life. By building more fully wheelchair accessible facilities, and purchasing outdoor adaptive equipment. Through these tools, the youth and those with disabilities will build lifetime memories and unforgettable tools for success. Finding their own potential and passions and going on to pursue them even when life knocks you down.</p>
    <p>This future facility would promote awareness to the community around it about the importance of humanity and education as well as providing inclusion and equality for those with disabilities.</p>
    <div class="thanks">We are so grateful and truly appreciate your generous donations. Together we can reach it!</div>
    <div class="photo waterfall" role="img" aria-label="Photo of a man in a wheelchair with a friend beside a waterfall"></div>
  </div>

  <div class="panel panel--cream">
    <h2>Breakdown of the first phase of building this enhanced accessible facility.</h2>
    <ul class="steps">
      <li>Archaeological summary</li>
      <li>Site survey</li>
      <li>Fulfill legal notification requirements to existing neighbors</li>
      <li>Traffic Impact analysis</li>
      <li>Drainage and Erosion Control analysis</li>
      <li>Waste Water System Design</li>
      <li>Topographical Design Survey</li>
      <li>Construction Permitting Phase</li>
      <li>Infrastructure</li>
      <li>Water systems/irrigation</li>
      <li>Sewage tanks and systems</li>
      <li>Excavating and Leveling</li>
      <li>Road Parking</li>
    </ul>
    <div class="photo stage-photo-a" role="img" aria-label="Photo of a man in a wheelchair preparing adaptive equipment"></div>
    <div class="photo stage-photo-b" role="img" aria-label="Photo of a speaker in a wheelchair on stage with a microphone"></div>
  </div>

  <div class="panel">
    <p>53 million individuals with disabilities live in the United States and one billion people with disabilities live around the world. Families that experience catastrophic events or individuals born with developmental disabilities face enormous challenges. Many families that experience this are financially destroyed and spiritually as well as emotionally exhausted. One of the biggest struggles those with disabilities face is getting enough education. Most individuals with disabilities often are left to feel isolated and alone. Everyone in their life time is at risk of mobility impairment. This could happen any day, at anytime to anyone.</p>
    <div class="duo">
      <div class="photo portrait-a" role="img" aria-label="Black and white photo of a young man outdoors"></div>
      <div class="photo portrait-b" role="img" aria-label="Photo of a young man recovering in hospital"></div>
    </div>
    <p>Dale Morrow lost the use of his legs after an accident as a young man. With the support of family and friends he learned new ways to work, travel and play, and found fresh goals along the way. Today he volunteers with our board, sharing his hope and practical advice with families who are just starting down the same road.</p>
    <div class="logo inside-logo"><span class="logo-dot"></span>Camp Bright Reach Maui</div>
  </div>

  <svg class="waves" viewBox="0 0 760 90" preserveAspectRatio="none" aria-hidden="true">
    <path d="M0 50 Q130 20 253 48 Q380 75 507 40 Q640 10 760 36 L760 90 L0 90Z" fill="var(--green)"/>
    <path d="M0 46 Q130 16 253 44 Q380 71 507 36 Q640 6 760 32" fill="none" stroke="var(--blue)" stroke-width="2"/>
  </svg>
</section>

</body>
</html>
```